6 - 8 'Holistic' Instagram Graphics

Hi there!
We are looking to build up a library of Graphic Templates to use as Instagram & Facebook posts for our Holistic Medi Spa (& 3 other companies eventually)
This competition is for a sample of 6 - 8 designs. For the winner(s), we will make an agreement for a batch order (Looking for 200+ designs in total), and will be looking to make a long term arrangement.
Please find a full job description in the attached Word Document.
Any questions, don't hesitate to ask.
Thanks!
Medical Spa

```html
<!DOCTYPE html>
<html lang="en">
<head>
<meta charset="utf-8">
<title>Lumen Grove – Holistic Medi Spa Social Posts</title>
<link href="https://fonts.googleapis.com/css2?family=Poppins:wght@300;400;500&family=Tinos:ital,wght@0,400;1,400;1,700&display=swap" rel="stylesheet">
<style>
  :root {
    --page: #ffffff;
    --ink: #111111;
    --brand-grey: #8a8a86;
    --tan: #cdb48f;
    --mint: #e6f6f2;
    --teal: #7fcabe;
    --teal-line: #6ec3b4;
    --coral: #f07a69;
    --white: #ffffff;
  }
  * { margin: 0; padding: 0; box-sizing: border-box; }
  html, body { width: 1165px; height: 1200px; overflow: hidden; background: var(--page); }
  body { position: relative; font-family: "Poppins", sans-serif; color: var(--ink); }

  .post {
    position: absolute; width: 513px; height: 513px; overflow: hidden;
    box-shadow: 0 4px 14px rgba(0,0,0,0.08);
  }
  .post--massage { left: 44px; top: 63px; background: #fbfcfc; }
  .post--laser { left: 603px; top: 63px; background: var(--mint); }
  .post--contour { left: 44px; top: 627px; background: var(--mint); }
  .post--acne { left: 603px; top: 627px; background: var(--mint); }
  .post svg.shapes { position: absolute; left: 0; top: 0; }

  .brand { position: absolute; display: flex; align-items: center; gap: 10px; }
  .brand__dot { border-radius: 50%; border: 3px solid var(--brand-grey); flex: none; }
  .brand__name { font-family: "Poppins", sans-serif; font-weight: 300; color: var(--brand-grey); line-height: 1; white-space: nowrap; }
  .brand__tag { font-family: "Poppins", sans-serif; font-weight: 300; color: var(--brand-grey); letter-spacing: 0.12em; line-height: 1; margin-top: 6px; white-space: nowrap; }

  /* Post 1 */
  .post--massage .brand { left: 18px; top: 16px; }
  .post--massage .brand__dot { width: 62px; height: 62px; }
  .post--massage .brand__name { font-size: 33px; }
  .post--massage .brand__tag { font-size: 13px; }
  .offer-badge {
    position: absolute; left: 345px; top: 375px; width: 131px; height: 39px;
    background: var(--tan); border-radius: 20px; color: var(--white);
    font-size: 21px; font-weight: 500; display: flex; align-items: center; justify-content: center;
  }
  .service-title { position: absolute; left: 329px; width: 166px; top: 423px; text-align: center; font-size: 22px; font-weight: 500; letter-spacing: 0.02em; }
  .service-note { position: absolute; left: 322px; width: 180px; top: 455px; text-align: center; font-size: 8px; line-height: 12px; color: #222; }
  .tagline { position: absolute; left: 18px; top: 417px; font-family: "Tinos", serif; font-style: italic; font-size: 31px; line-height: 35px; }

  /* Post 2 */
  .post--laser .brand { left: 21px; top: 24px; gap: 8px; }
  .post--laser .brand__dot { width: 42px; height: 42px; }
  .post--laser .brand__name { font-size: 21px; }
  .post--laser .brand__tag { font-size: 8px; margin-top: 4px; }
  .quote { position: absolute; left: 12px; top: 132px; font-family: "Tinos", serif; font-style: italic; font-size: 21px; line-height: 31px; color: #1d1d1d; }
  .discount { position: absolute; left: 11px; top: 335px; color: var(--coral); font-family: "Poppins", sans-serif; font-size: 33px; font-weight: 400; line-height: 1; }
  .discount strong { font-style: italic; font-weight: 500; letter-spacing: -0.02em; }
  .laser-service { position: absolute; left: 11px; top: 380px; font-size: 16.5px; font-weight: 400; }

  /* Post 3 */
  .post--contour .brand { right: 18px; top: 28px; gap: 8px; }
  .post--contour .brand__dot { width: 30px; height: 30px; }
  .post--contour .brand__name { font-size: 20px; }
  .contour-offer { position: absolute; left: 21px; top: 380px; font-family: "Tinos", serif; font-size: 48px; line-height: 1; color: var(--white); }
  .contour-service { position: absolute; left: 21px; top: 443px; font-family: "Tinos", serif; font-size: 31px; line-height: 1; color: var(--white); white-space: nowrap; }

  /* Post 4 */
  .pool-photo { position: absolute; left: 0; top: 0; width: 269px; height: 513px; background: linear-gradient(180deg, #e2e3df 0%, #dcc5b4 45%, #cdb2a0 62%, #9fc3d2 80%, #8db6c9 100%); }
  .tan-bar { position: absolute; left: 354px; width: 71px; background: var(--tan); }
  .tan-bar--top { top: 0; height: 86px; }
  .tan-bar--bottom { top: 431px; height: 82px; }
  .acne-offer { position: absolute; left: 269px; width: 244px; top: 95px; text-align: center; font-family: "Tinos", serif; font-size: 33px; line-height: 1; }
  .acne-copy { position: absolute; left: 269px; width: 244px; top: 141px; text-align: center; font-size: 14.5px; font-weight: 500; line-height: 31.3px; text-transform: uppercase; }
  .post--acne .brand { left: 308px; top: 382px; gap: 6px; }
  .post--acne .brand__dot { width: 38px; height: 38px; }
  .post--acne .brand__name { font-size: 22px; }
  .post--acne .brand__tag { font-size: 8px; margin-top: 3px; }
</style>
</head>
<body>

<!-- Post 1: facial massage -->
<section class="post post--massage">
  <svg class="shapes" width="513" height="513" viewBox="0 0 513 513">
    <defs>
      <linearGradient id="massageTone" x1="0" y1="0" x2="1" y2="1">
        <stop offset="0" stop-color="#f3e2d2"/>
        <stop offset="0.5" stop-color="#ebc7b2"/>
        <stop offset="1" stop-color="#e2b9a2"/>
      </linearGradient>
    </defs>
    <path d="M0,130 C140,210 270,80 513,45 L513,60 C300,90 150,225 0,148 Z" fill="var(--tan)"/>
    <path role="img" aria-label="Photo of a woman receiving a relaxing facial massage with orchids and spa stones" d="M0,150 C150,228 290,95 513,60 L513,372 C420,405 300,410 210,398 C120,386 50,355 0,322 Z" fill="url(#massageTone)"/>
    <path d="M0,322 C50,355 120,386 210,398 C300,410 420,405 513,372" fill="none" stroke="var(--teal-line)" stroke-width="2"/>
  </svg>
  <div class="brand">
    <span class="brand__dot"></span>
    <div>
      <div class="brand__name">Lumen Grove</div>
      <div class="brand__tag">HOLISTIC MEDI SPA</div>
    </div>
  </div>
  <div class="offer-badge">40%OFF</div>
  <h2 class="service-title">MEDI-SPA</h2>
  <p class="service-note">his revolution in skin tightening offers a powerful solution for treating fine lines, wrinkles &amp; blemishes.</p>
  <p class="tagline">A healthy outside<br>starts from the inside</p>
</section>

<!-- Post 2: laser hair removal -->
<section class="post post--laser">
  <svg class="shapes" width="513" height="513" viewBox="0 0 513 513">
    <defs>
      <linearGradient id="clinicTone" x1="0" y1="0" x2="1" y2="1">
        <stop offset="0" stop-color="#f4f5f4"/>
        <stop offset="1" stop-color="#e8dcd3"/>
      </linearGradient>
      <linearGradient id="faceTone" x1="0" y1="0" x2="1" y2="1">
        <stop offset="0" stop-color="#f6e2db"/>
        <stop offset="1" stop-color="#e8c4b8"/>
      </linearGradient>
      <linearGradient id="candleTone" x1="0" y1="0" x2="0" y2="1">
        <stop offset="0" stop-color="#b68a6c"/>
        <stop offset="1" stop-color="#7a5a48"/>
      </linearGradient>
    </defs>
    <circle role="img" aria-label="Photo of a specialist giving a cosmetic skin treatment" cx="376" cy="269" r="147" fill="url(#clinicTone)" stroke="var(--teal-line)" stroke-width="4"/>
    <circle role="img" aria-label="Photo of a facial laser device treatment" cx="318" cy="95" r="67" fill="url(#faceTone)" stroke="var(--teal-line)" stroke-width="4"/>
    <circle role="img" aria-label="Photo of a smiling woman relaxing by candlelight" cx="318" cy="419" r="67" fill="url(#candleTone)" stroke="var(--teal-line)" stroke-width="4"/>
  </svg>
  <div class="brand">
    <span class="brand__dot"></span>
    <div>
      <div class="brand__name">Lumen Grove</div>
      <div class="brand__tag">HOLISTIC MEDI SPA</div>
    </div>
  </div>
  <p class="quote">“Wellness Encompasses<br>A Healthy Body, A Sound<br>Mind And A Tranquil<br>Spirit. Enjoy The<br>Journey As You Strive<br>For Wellness.”</p>
  <p class="discount"><strong>22%</strong> OFF</p>
  <p class="laser-service">LASER HAIR REMOVAL</p>
</section>

<!-- Post 3: RF body contouring -->
<section class="post post--contour">
  <svg class="shapes" width="513" height="513" viewBox="0 0 513 513">
    <defs>
      <linearGradient id="bodyTone" x1="0" y1="0" x2="1" y2="1">
        <stop offset="0" stop-color="#f3d8ca"/>
        <stop offset="1" stop-color="#e9c3b0"/>
      </linearGradient>
    </defs>
    <path role="img" aria-label="Photo of a woman in neutral sportswear posing against a peach wall" d="M0,0 H513 V170 C495,265 400,342 260,346 C150,349 60,305 0,255 Z" fill="url(#bodyTone)"/>
    <path d="M0,298 C100,358 200,380 305,378 C400,376 470,348 513,315 V513 H0 Z" fill="var(--teal)"/>
  </svg>
  <div class="brand">
    <span class="brand__dot"></span>
    <div class="brand__name">Lumen Grove</div>
  </div>
  <p class="contour-offer">25% OFF</p>
  <p class="contour-service">RF BODY CONTOURING</p>
</section>

<!-- Post 4: acne treatment -->
<section class="post post--acne">
  <div class="pool-photo" role="img" aria-label="Photo of a woman relaxing at the edge of a spa pool resting on a rolled towel"></div>
  <div class="tan-bar tan-bar--top"></div>
  <p class="acne-offer">25% OFF</p>
  <p class="acne-copy">A powerful<br>treatment in<br>combating acne,<br>smoothing blemishes<br>and reducing the<br>presence of large<br>pores.</p>
  <div class="brand">
    <span class="brand__dot"></span>
    <div>
      <div class="brand__name">Lumen Grove</div>
      <div class="brand__tag">HOLISTIC MEDI SPA</div>
    </div>
  </div>
  <div class="tan-bar tan-bar--bottom"></div>
</section>

</body>
</html>
```